Professional Label needed for Velvet Biscuit Kitchen

I make 100% organic dog treats. Wheat and gluten free.

I will be packaging them in a window kraft bag. I need a nicely designed label to place on each bag. The name of my company is The Velvet Biscuit Kitchen Company. All ingredients are organic and no preservatives are used. They are a healthy alternative to "assembly line" treats made by large companies.

Target Market(s)

Dog Owners

Industry/Entity Type

Pet

Font styles to use
Serif

Colors
00a990

Requirements
Must have
• can use a dog paw - see attached files. Dog themed, 100%
• Organic Dog Treats.
• No preservatives, nothing artificial, no corn, wheat or soy, made in Texas, USA with 100% organic ingredients. Non GMO
• Must have "dog treat" somewhere.
• "The Velvet Biscuit Kitchen Co." font size needs to be bigger than anything else.
Nice to have
• I like teal and brown
• I'm open to anything really as long as its dog themed

```html
<!DOCTYPE html>
<html lang="en">
<head>
<meta charset="utf-8">
<title>The Velvet Biscuit Kitchen Co. – Dog Treat Label</title>
<link href="https://fonts.googleapis.com/css2?family=Fjalla+One&family=Open+Sans:wght@700;800&family=Bitter:wght@700&display=swap" rel="stylesheet">
<style>
  :root {
    --teal: #00a990;
    --kraft: #c4b090;
    --kraft-dark: #a99572;
    --tan: #dcc8a6;
    --cocoa: #4b4340;
    --cream: #ffffff;
    --backdrop: #eceeef;
  }
  html, body {
    margin: 0;
    padding: 0;
    width: 792px;
    height: 1200px;
    overflow: hidden;
    background: var(--backdrop);
  }
  .canvas {
    width: 792px;
    height: 1200px;
    display: flex;
    align-items: center;
    justify-content: center;
  }
  .label { width: 680px; height: 693px; display: block; }
  .brand-arc {
    font-family: "Fjalla One", sans-serif;
    font-size: 23px;
    fill: var(--cream);
    letter-spacing: 0.2px;
  }
  .ribbon-pct { font-family: "Open Sans", sans-serif; font-weight: 800; font-size: 17px; fill: var(--cream); }
  .ribbon-line { font-family: "Open Sans", sans-serif; font-weight: 800; font-size: 13px; fill: var(--cream); }
  .plate-text { font-family: "Bitter", serif; font-weight: 700; font-size: 9.5px; fill: var(--cocoa); }
  .origin { font-family: "Bitter", serif; font-weight: 700; font-size: 7.5px; fill: var(--cocoa); }
  .badge-text { font-family: "Open Sans", sans-serif; font-weight: 800; font-size: 4.6px; fill: var(--cream); }
</style>
</head>
<body>
<main class="canvas">
<svg class="label" viewBox="0 0 360 367" xmlns="http://www.w3.org/2000/svg" aria-label="The Velvet Biscuit Kitchen Co. dog treat label">
  <defs>
    <symbol id="paw" viewBox="0 0 20 20">
      <ellipse cx="10" cy="13.5" rx="5.2" ry="4.4" fill="var(--cream)"/>
      <ellipse cx="3.4" cy="8" rx="2.2" ry="2.8" fill="var(--cream)"/>
      <ellipse cx="7.6" cy="4" rx="2.2" ry="2.8" fill="var(--cream)"/>
      <ellipse cx="12.4" cy="4" rx="2.2" ry="2.8" fill="var(--cream)"/>
      <ellipse cx="16.6" cy="8" rx="2.2" ry="2.8" fill="var(--cream)"/>
    </symbol>
    <path id="brand-path" d="M 64 178 A 118 118 0 0 1 300 178"/>
    <path id="badge1" d="M 201 335 A 14 14 0 0 1 229 335"/>
    <path id="badge2" d="M 249 335 A 14 14 0 0 1 277 335"/>
    <path id="badge3" d="M 311 335 A 14 14 0 0 1 339 335"/>
  </defs>

  <!-- kraft frame and teal field -->
  <rect class="frame" x="0" y="0" width="360" height="367" fill="var(--kraft)"/>
  <rect class="field" x="8" y="8" width="344" height="351" fill="var(--teal)"/>

  <!-- medallion -->
  <ellipse cx="182" cy="178" rx="106" ry="96" fill="var(--cocoa)"/>
  <ellipse cx="182" cy="178" rx="100" ry="90" fill="var(--tan)"/>
  <rect role="img" aria-label="Playful dog with a bone illustration" x="112" y="96" width="140" height="84" rx="38" fill="#cdb794"/>

  <!-- brand name on arc, above the medallion -->
  <text class="brand-arc"><textPath href="#brand-path" startOffset="50%" text-anchor="middle">THE VELVET BISCUIT KITCHEN CO.</textPath></text>

  <!-- paws -->
  <use href="#paw" x="30" y="30" width="20" height="20"/>
  <use href="#paw" x="312" y="30" width="20" height="20"/>
  <use href="#paw" x="96" y="168" width="16" height="16"/>
  <use href="#paw" x="252" y="168" width="16" height="16"/>
  <use href="#paw" x="28" y="206" width="20" height="20"/>
  <use href="#paw" x="318" y="206" width="20" height="20"/>
  <use href="#paw" x="146" y="313" width="20" height="20"/>

  <!-- ribbon banner -->
  <path class="ribbon-tail" d="M 78 222 L 50 228 L 62 242 L 52 258 L 88 252 Z" fill="var(--kraft-dark)" stroke="var(--cocoa)" stroke-width="1.4"/>
  <path class="ribbon-tail" d="M 286 222 L 314 228 L 302 242 L 312 258 L 276 252 Z" fill="var(--kraft-dark)" stroke="var(--cocoa)" stroke-width="1.4"/>
  <path class="ribbon" d="M 76 192 Q 182 168 288 192 L 288 236 Q 182 212 76 236 Z" fill="var(--kraft)" stroke="var(--cocoa)" stroke-width="1.6"/>
  <text class="ribbon-pct" x="182" y="201" text-anchor="middle">100%</text>
  <text class="ribbon-line" x="182" y="218" text-anchor="middle">organic ingredients</text>

  <!-- dog treats plate -->
  <path class="plate" d="M 130 246 Q 182 238 234 246 L 226 272 Q 182 266 138 272 Z" fill="var(--tan)" stroke="var(--cocoa)" stroke-width="1.4"/>
  <text class="plate-text" x="182" y="262" text-anchor="middle">DOG TREATS</text>

  <!-- stars -->
  <path d="M 72 268 l 2.2 4.6 5 .6 -3.7 3.4 1 5 -4.5 -2.5 -4.5 2.5 1 -5 -3.7 -3.4 5 -.6 Z" fill="var(--cocoa)"/>
  <path d="M 295 268 l 2.2 4.6 5 .6 -3.7 3.4 1 5 -4.5 -2.5 -4.5 2.5 1 -5 -3.7 -3.4 5 -.6 Z" fill="var(--cocoa)"/>

  <!-- origin -->
  <text class="origin" x="16" y="348">MADE IN TEXAS, USA</text>

  <!-- claim icons -->
  <g class="claim" fill="none" stroke="var(--cream)" stroke-width="2.4">
    <circle cx="215" cy="341" r="10"/><line x1="208" y1="334" x2="222" y2="348"/>
    <circle cx="263" cy="341" r="10"/><line x1="256" y1="334" x2="270" y2="348"/>
    <circle cx="325" cy="341" r="10"/><line x1="318" y1="334" x2="332" y2="348"/>
  </g>
  <text class="badge-text"><textPath href="#badge1" startOffset="50%" text-anchor="middle">No GMO</textPath></text>
  <text class="badge-text"><textPath href="#badge2" startOffset="50%" text-anchor="middle">No ARTIFICIAL</textPath></text>
  <text class="badge-text"><textPath href="#badge3" startOffset="50%" text-anchor="middle">No PRESERVATIVES</textPath></text>
</svg>
</main>
</body>
</html>
```